Music Festival in Colorado Needs Awesome Flier Design

We need an eye-catching & captivating flier design for an annual music festival in Denver, CO (USA). The festival features the best Colorado musicians within the genres of jam - funk - bluegrass - electronic - reggae - rock.

The design should look clean and professional while still being creative and unique. The past three years' flier designs are attached, as well as the logo and some other designs that match the aesthetic of what we're looking for.

This festival has a big element of Colorado pride so any

Target Market(s)

Hippies - live music enthusiasts - partiers. Ages 21 - 40.

Industry/Entity Type

Entertainment

Colors
0355a3
ec1f27
ffffff
fbed22

Requirements
Must have
• Attached design text.
Nice to have
• - Quality texture and psychedelic elements.
• - Colorado pride elements; color scheme (red, white, blue & yellow), flag, ect.
• - Nature elements are awesome but this is also a downtown festival so keep that in mind.
Should not have
• Cheesy artwork.

```html
<!DOCTYPE html>
<html lang="en">
<head>
<meta charset="utf-8">
<title>Pass the Sound – Colorado Music Festival</title>
<link rel="stylesheet" href="https://fonts.googleapis.com/css2?family=Kaushan+Script&family=Oswald:wght@500;600;700&display=swap">
<style>
  :root {
    --sky-top: #ee7f22;
    --sky-mid: #f6a33a;
    --dusk: #c2506a;
    --ridge: #5a3a7a;
    --night: #0f1f4a;
    --night-deep: #0b1838;
    --sun: #fbed22;
    --ink: #1a1a1a;
    --cream: #ffffff;
    --accent-red: #b8221c;
  }
  * { margin: 0; padding: 0; box-sizing: border-box; }
  html, body { width: 849px; height: 1200px; overflow: hidden; background: var(--night-deep); }
  .poster {
    position: relative;
    width: 849px; height: 1200px;
    overflow: hidden;
    font-family: "Oswald", sans-serif;
    background: var(--night-deep);
  }
  .landscape {
    position: absolute; left: 0; top: 0;
    width: 849px; height: 720px;
    background: linear-gradient(180deg,
      var(--sky-top) 0%,
      var(--sky-mid) 38%,
      var(--dusk) 58%,
      var(--ridge) 72%,
      var(--night) 88%,
      var(--night-deep) 100%);
  }
  .edition {
    position: absolute; top: 18px; width: 100%;
    text-align: center;
    font-family: "Kaushan Script", cursive;
    font-size: 50px; color: var(--sun);
  }
  .dates {
    position: absolute; top: 92px; width: 100%;
    text-align: center;
    font-weight: 600; font-size: 20px; letter-spacing: 2px;
    color: var(--accent-red);
  }
  .festival-name {
    position: absolute; top: 190px; width: 100%;
    text-align: center;
    font-weight: 700; font-size: 84px; line-height: 1;
    letter-spacing: 2px; color: var(--ink);
    text-transform: uppercase;
  }
  .festival-tag {
    position: absolute; top: 292px; width: 100%;
    text-align: center;
    font-weight: 700; font-size: 20px; letter-spacing: 6px;
    color: var(--ink); text-transform: uppercase;
  }
  .lineup {
    position: absolute; left: 50px; right: 40px; top: 652px;
    color: var(--cream);
  }
  .headliner {
    font-weight: 700; font-size: 84px; line-height: 1;
    text-transform: uppercase; letter-spacing: 1px;
  }
  .act-row {
    font-weight: 600; line-height: 1.2; white-space: nowrap;
  }
  .act-row span + span::before { content: " • "; }
  .act-row span:first-child::before { content: "• "; }
  .row-lg { font-size: 42px; margin-top: 10px; }
  .row-md { font-size: 31px; margin-top: 8px; }
  .row-sm { font-size: 29px; margin-top: 6px; }
  .venue {
    position: absolute; left: 56px; top: 1070px;
    font-weight: 500; font-size: 16px; line-height: 1.35;
    color: var(--sun);
  }
  .tickets {
    position: absolute; right: 40px; top: 1068px;
    text-align: right; color: var(--cream);
  }
  .tickets-label { font-weight: 500; font-size: 20px; letter-spacing: 3px; text-transform: uppercase; }
  .tickets-url { font-weight: 700; font-size: 32px; color: var(--sun); margin-top: 2px; }
</style>
</head>
<body>
<div class="poster">
  <div class="landscape" role="img" aria-label="Sunset illustration: orange sky, setting yellow sun and layered purple mountain ridges with pine trees fading into night"></div>

  <div class="edition">6th Annual</div>
  <div class="dates">MAY 11TH - 13TH, 2018</div>

  <div class="festival-name">Pass the Sound</div>
  <div class="festival-tag">Colorado Music Festival</div>

  <div class="lineup">
    <div class="headliner">Cole Harper Band</div>
    <div class="act-row row-lg"><span>Open Sky Orchestra</span><span>Fault Theory</span></div>
    <div class="act-row row-lg"><span>The Lucky Sprouts</span><span>J-Ray &amp; The Summit</span></div>
    <div class="act-row row-md"><span>Tallgrass</span><span>Kinetics</span><span>Radiance Ensemble</span><span>Sunwashed</span></div>
    <div class="act-row row-sm"><span>Polytones</span><span>Kaleido</span><span>Clear Signal</span><span>Rail Junction</span><span>Orbits</span></div>
  </div>

  <div class="venue">
    Elm Yard Commons<br>
    412 W. 52nd Ave<br>
    Denver, CO 80216
  </div>

  <div class="tickets">
    <div class="tickets-label">Tickets &amp; more info @</div>
    <div class="tickets-url">www.passthesoundfest.com</div>
  </div>
</div>
</body>
</html>
```